Create a highly polished design and structured Sales Agreement template

We need a professionally designed Sales Agreement template for our company, Calvern Metrics, Inc. This template will be used to formalize agreements with our customers for calibration services. The design should reflect the high standards and professionalism of a Palisade 200 company.
Key requirements:
Incorporate our company logo and branding elements.
Ensure the template includes sections for all critical details such as customer name, address, services provided, pricing, and terms of payment.
The layout should be clean, modern, and easy to navigate.
Include placeholders for variable information (e.g., customer name, address, etc.) that can be easily filled out for each customer.
Design the template in a way that allows our team to update it easily via a form entry system.
Ensure the language and formatting are polished and professional.
We have attached our current Sales Agreement for reference. Please maintain all key details while enhancing the structure, format, and overall presentation.

```html
<!DOCTYPE html>
<html lang="en">
<head>
<meta charset="utf-8">
<title>Sales Agreement – Calvern Metrics, Inc.</title>
<link href="https://fonts.googleapis.com/css2?family=Questrial&family=Tinos:wght@400;700&display=swap" rel="stylesheet">
<style>
  :root{
    --backdrop:#6e706f;
    --paper:#ffffff;
    --teal:#4e9682;
    --band:#e0e8e6;
    --rail:#b9d3cc;
    --ink:#1d1d1d;
    --rule:#9a9a9a;
  }
  *{margin:0;padding:0;box-sizing:border-box}
  html,body{width:1015px;height:1200px;overflow:hidden}
  body{background:var(--backdrop);position:relative;font-family:"Tinos",serif;color:var(--ink)}
  .page{position:absolute;width:399px;height:516px;background:var(--paper);overflow:hidden}
  .page--cover{left:522px;top:71px}
  .page--terms{left:94px;top:613px}
  .page--closing{left:522px;top:613px}
  .rail{position:absolute;left:28.5px;top:0;bottom:0;width:1px;background:var(--rail)}
  .page--cover .rail{top:82px}
  .doc-title{position:absolute;left:29px;top:34px;font-family:"Questrial",sans-serif;font-size:23px;letter-spacing:.5px;color:var(--teal);font-weight:400}
  .brand{position:absolute;right:24px;top:36px;text-align:right}
  .brand__lockup{display:flex;align-items:center;gap:4px}
  .brand__dot{width:10px;height:10px;border-radius:50%;background:var(--teal)}
  .brand__name{font-size:9px;font-weight:700;color:var(--teal);white-space:nowrap}
  .brand__tag{font-size:4.5px;margin-top:5px;color:var(--ink)}
  .parties{position:absolute;left:0;top:82px;width:399px;height:146px;background:var(--band);font-size:7.4px;line-height:13.3px;padding:13px 0 0 47px}
  .parties__lead{margin-bottom:5px}
  .party{display:grid;grid-template-columns:38px 8px auto;margin-bottom:8px}
  .party dt{font-weight:700}
  .section{position:absolute;left:47px;width:306px;font-size:7.4px;line-height:9.1px}
  .page--terms .section,.page--closing .section{width:296px}
  .section::before{content:"";position:absolute;left:-23px;top:1px;width:9.5px;height:9.5px;border-radius:50%;background:var(--teal)}
  .section h2{font-size:9.2px;font-weight:700;color:var(--teal);letter-spacing:.2px;margin-bottom:4px}
  .justify{text-align:justify}
  .section ol{margin:4px 0 0 12px;padding-left:12px}
  .section ol li{margin-bottom:4px;padding-left:2px}
  .section ul{margin:0 0 0 12px;padding-left:12px}
  .spaced li{margin-bottom:4.5px}
  .compact li{margin-bottom:2px}
  .tight li{margin-bottom:0}
  .plain{position:absolute;left:47px;width:306px;font-size:7.4px;line-height:9px}
  .plain ul{margin-left:12px;padding-left:12px}
  .hr{position:absolute;left:47px;width:306px;height:1px;background:var(--rule)}
  .sig-label{font-weight:700}
  .sub{font-weight:700;margin-bottom:5px}
</style>
</head>
<body>

<section class="page page--cover">
  <h1 class="doc-title">SALES AGREEMENT</h1>
  <div class="brand">
    <div class="brand__lockup">
      <span class="brand__dot"></span>
      <span class="brand__name">Calvern Metrics</span>
    </div>
    <div class="brand__tag">An Orrin Labs Company</div>
  </div>
  <div class="parties">
    <p class="parties__lead">This Sales Agreement (the "Agreement") is made and entered into as of [Date] by and between:</p>
    <dl class="party">
      <dt>Seller</dt><dt>:</dt>
      <dd>Calvern Metrics, Inc.<br>4180 N Larkspur Ave, Suite B Meridian, ID 83646<br>Phone: 800-555-0147</dd>
    </dl>
    <dl class="party">
      <dt>Customer</dt><dt>:</dt>
      <dd>[Customer Name]<br>[Customer Address]<br>[Customer City, State, Zip]<br>Phone: [Customer Phone] Email: [Customer Email]</dd>
    </dl>
  </div>
  <div class="rail"></div>

  <div class="section" style="top:245px">
    <h2>INTRODUCTION</h2>
    <p class="justify">Calvern Metrics, Inc., an ISO/IEC 17025 accredited calibration laboratory accredited by NMAB, is committed to providing high-quality calibration services. With over 30 years of experience, we are recognized nationally for our expertise and reliability.</p>
  </div>
  <div class="section" style="top:298px">
    <h2>SERVICES</h2>
    <p>Calvern Metrics, Inc. agrees to provide the following services to [Customer Name]:</p>
    <ol>
      <li><b>Calibration Services</b>: Full-time on-site trained technician support.</li>
      <li class="justify"><b>Turn-key Service Management</b>: Scheduling, on-site calibrations, pick-up and delivery, turn time management, and interface with selected vendors.</li>
      <li><b>Document Control</b>: Online access to calibration documents via our website.</li>
    </ol>
  </div>
  <div class="section" style="top:381px">
    <h2>TECHNICIAN GROUP</h2>
    <p class="justify">A pool of qualified technicians ensures uninterrupted service. A dedicated technician, along with an assigned backup technician, will perform calibrations either on-site or at our lab, minimizing costly delays.</p>
  </div>
  <div class="section" style="top:434px">
    <h2>ISO/IEC 17025 ACCREDITATION</h2>
    <p>Our accreditation ensures that we consistently deliver the quality and reliability that our customers <b>expect.</b></p>
  </div>
</section>

<section class="page page--terms">
  <div class="rail"></div>
  <div class="section" style="top:48px">
    <h2>DOCUMENT CONTROL</h2>
    <p>Calibration documents will be accessible online at [Company Website], allowing designated employees of [Customer Name] to view and print calibration data and certificates instantly. In the event of service termination, access will continue for 90 business days for obtaining status reports.</p>
  </div>
  <div class="section" style="top:110px">
    <h2>SERVICE INTEGRATION</h2>
    <p>Calvern Metrics, Inc. will collaborate closely with [Customer Name]’s designated personnel, handling the calibration workload. Outsourced items will be billed at cost plus 25%, covering shipping, insurance, and documentation costs.</p>
  </div>
  <div class="section" style="top:163px">
    <h2>MAINTENANCE &amp; SUPPORT</h2>
    <p>We will provide repair services for the following types of M&amp;TE, quoted separately:</p>
    <ul class="tight">
      <li>Dimensional Hand Tools</li><li>Handheld Meters</li><li>Lab Equipment</li><li>Weighing Equipment</li><li>Compression Machines</li>
    </ul>
  </div>
  <div class="section" style="top:243px">
    <h2>QUALITY ASSURANCE</h2>
    <p>Quality will be monitored through calibration documentation review, technician testing, and vendor audits.</p>
  </div>
  <div class="section" style="top:287px">
    <h2>PRICING</h2>
    <p class="sub">Dedicated On-site Technician (3 Days per Week)</p>
    <ul class="spaced">
      <li>Monthly Charge: $12,500.00</li><li>Yearly Total: $150,000.00</li><li>Sales tax not included.</li><li>Potential annual price increase of 3% beginning the second year.</li>
    </ul>
  </div>
  <div class="section" style="top:377px">
    <h2>TERMS OF PAYMENT</h2>
    <ul class="spaced" style="margin-top:5px">
      <li>Net 30 terms of payment.</li><li>Opt-out available with 90 days written notice.</li>
    </ul>
  </div>
  <div class="section" style="top:423px">
    <h2>KEY POINTS</h2>
    <ul class="spaced" style="margin-top:5px">
      <li>Primary on-site days chosen by [Customer Name].</li><li>Monthly custom reports on equipment due for calibration.</li><li>Dedicated and backup technicians to learn your business.</li>
    </ul>
  </div>
</section>

<section class="page page--closing">
  <div class="rail"></div>
  <div class="plain" style="top:47px">
    <ul class="compact">
      <li>All calibrations due at the end of the month.</li>
      <li>Customization of Trackwell software for equipment tracking and reports.</li>
      <li>Use and efficiency with [Customer Name]’s equipment tracking software.</li>
      <li>Outsourced items billed at cost plus 25%.</li>
      <li>This price is based on a 2-year contract.</li>
    </ul>
  </div>
  <div class="section" style="top:114px">
    <h2>FINAL STATEMENT</h2>
    <p>Calvern Metrics, Inc. will provide a dedicated on-site technician 3 days a week to handle calibrations and third-party outsourcing, ensuring all monthly due dates are met efficiently. Our goal is to provide seamless support without interfering with production.</p>
  </div>
  <div class="hr" style="top:171px"></div>
  <p class="plain sig-label" style="top:183px">SIGNATURES</p>
  <p class="plain sig-label" style="top:201px">Calvern Metrics, Inc.:</p>
  <div class="hr" style="top:226px"></div>
  <p class="plain" style="top:238px">[Authorized Signatory Name]<br>[Title]<br>Date: _______________</p>
  <p class="plain sig-label" style="top:274px">[Customer Name]:</p>
  <div class="hr" style="top:298px"></div>
  <p class="plain" style="top:310px">[Authorized Signatory Name]<br>[Title]<br>Date: _______________</p>
</section>

</body>
</html>
```